Banner signature

Hi, looking for a banner for email signature 728 px wide and 200 px high
Could we have our 10 year logo and premium logo, a similar look and feel of our previous banner design (I've attached) and also include an aboriginal design with the Wording
This email comes to you from Gubbi Gubbi country
I've attached an example of some look and feels that we like.
Can we have the background of banner the Blue colour of our Fern & Tide logo and

```html
<!DOCTYPE html>
<html lang="en">
<head>
<meta charset="utf-8">
<title>Fern &amp; Tide – Email Signature Banner</title>
<link rel="stylesheet" href="https://fonts.googleapis.com/css2?family=Kalam:wght@700&family=Chewy&display=swap">
<style>
  :root {
    --page: #ffffff;
    --frame: #e2e2e2;
    --navy: #1c1f4a;
    --sky: #27ace3;
    --gold: #d9b24a;
    --gold-light: #f1d47a;
    --ring-yellow: #f4d33c;
    --sun: #fbe23a;
    --ink-white: #ffffff;
  }
  * { margin: 0; padding: 0; box-sizing: border-box; }
  html, body {
    width: 1200px; height: 1200px; overflow: hidden;
    background: var(--page);
  }
  .banner {
    position: absolute; left: 163px; top: 480px;
    width: 873px; height: 240px;
    border: 1px solid var(--frame);
    background: var(--page);
    overflow: hidden;
  }
  .banner__art { position: absolute; inset: 0; }
  .brand-name {
    position: absolute; left: 104px; top: 130px;
    transform: translate(-50%, -50%);
    font-family: "Kalam", cursive;
    font-weight: 700; font-size: 19px; line-height: 1;
    color: var(--navy); white-space: nowrap;
  }
  .acknowledgement {
    position: absolute; left: 665px; top: 0;
    transform: translateX(-50%);
    width: 340px; height: 240px;
    text-align: center; color: var(--ink-white);
    font-family: "Kalam", cursive; font-weight: 700;
  }
  .acknowledgement__line {
    position: absolute; left: 0; right: 0;
    font-size: 25px; line-height: 1;
  }
  .acknowledgement__line--first { top: 41px; }
  .acknowledgement__line--second { top: 72px; }
  .acknowledgement__country {
    position: absolute; left: 0; right: 0; top: 114px;
    font-family: "Chewy", cursive; font-weight: 400;
    font-size: 48px; line-height: 1; letter-spacing: 1px;
    color: var(--sun);
  }
  .acknowledgement__line--last { top: 164px; }
  .wave { position: absolute; top: 79px; }
  .wave--left { left: 12px; }
  .wave--right { right: 12px; }
</style>
</head>
<body>
  <div class="banner">
    <svg class="banner__art" width="873" height="240" viewBox="0 0 873 240">
      <rect class="sky-panel" x="377" y="0" width="496" height="240" fill="var(--sky)" role="img" aria-label="Blue panel with Aboriginal dot artwork"/>
      <rect class="navy-band" x="66" y="0" width="78" height="240" fill="var(--navy)"/>
      <circle class="premium-seal" cx="104" cy="130" r="68" fill="var(--gold)"/>
      <circle class="anniversary-backdrop" cx="330" cy="120" r="120" fill="var(--page)"/>
      <circle class="anniversary-ring" cx="330" cy="120" r="94" fill="none" stroke="var(--ring-yellow)" stroke-width="3"/>
      <circle class="anniversary-badge" cx="330" cy="120" r="72" fill="var(--gold-light)" role="img" aria-label="Ten year anniversary badge"/>
    </svg>

    <div class="brand-name">Fern &amp; Tide</div>

    <div class="acknowledgement">
      <p class="acknowledgement__line acknowledgement__line--first">This email comes</p>
      <svg class="wave wave--left" width="44" height="12" viewBox="0 0 44 12">
        <path d="M2 6 q5 -6 10 0 t10 0 t10 0 t10 0" fill="none" stroke="var(--ink-white)" stroke-width="3" stroke-linecap="round"/>
      </svg>
      <p class="acknowledgement__line acknowledgement__line--second">to you from</p>
      <svg class="wave wave--right" width="44" height="12" viewBox="0 0 44 12">
        <path d="M2 6 q5 -6 10 0 t10 0 t10 0 t10 0" fill="none" stroke="var(--ink-white)" stroke-width="3" stroke-linecap="round"/>
      </svg>
      <p class="acknowledgement__country">GUBBI GUBBI</p>
      <p class="acknowledgement__line acknowledgement__line--last">country</p>
    </div>
  </div>
</body>
</html>
```